Stationary Design

Harbor Stagecraft Collective, Inc
27410 Marlowe Blvd Ste 4, Santa Fe Springs, CA 90512
Office: 213-584-2760 Email: admin@hsccrew.example

Industry/Entity Type

Entertainment

Colors
0054AA
0677BA
7BADD7
CADEEF
E8F1F8

```html
<!DOCTYPE html>
<html lang="en">
<head>
<meta charset="utf-8">
<title>Harbor Stagecraft Collective — Letterhead</title>
<link href="https://fonts.googleapis.com/css2?family=Montserrat:wght@400;600;700&display=swap" rel="stylesheet">
<style>
  :root {
    --brand-blue: #0054AA;
    --brand-mid: #0677BA;
    --brand-light: #7BADD7;
    --brand-pale: #CADEEF;
    --brand-mist: #E8F1F8;
    --ink: #2b2b2b;
    --grey-band: #9a9a9b;
    --backdrop: #e6e6e7;
    --paper: #ffffff;
  }
  * { margin: 0; padding: 0; box-sizing: border-box; }
  html, body {
    width: 1200px; height: 874px; overflow: hidden;
    background: var(--backdrop);
    font-family: "Montserrat", Arial, sans-serif;
    color: var(--ink);
  }
  .letterhead {
    position: absolute; left: 303px; top: 17px;
    width: 594px; height: 840px;
    background: var(--paper);
    box-shadow: 0 6px 24px rgba(0,0,0,.12);
    overflow: hidden;
  }
  .masthead {
    position: absolute; left: 44px; right: 44px; top: 40px;
    height: 72px;
    border-bottom: 1.5px solid var(--brand-blue);
  }
  .brand {
    position: absolute; left: 0; top: 10px;
    display: flex; align-items: center; gap: 10px;
  }
  .brand-mark {
    width: 34px; height: 34px; border-radius: 50%;
    background: var(--brand-blue);
  }
  .brand-name {
    font-size: 15px; font-weight: 700; color: var(--brand-blue);
    letter-spacing: .3px; line-height: 1.15; text-transform: uppercase;
  }
  .contact {
    position: absolute; right: 0; top: 0;
    padding-left: 14px;
    border-left: 1.5px solid var(--brand-blue);
    font-size: 8.5px; line-height: 1.45;
  }
  .contact-company {
    font-weight: 700; color: var(--brand-blue); text-transform: uppercase;
    font-size: 8px; margin-bottom: 2px;
  }
  .contact-row { display: flex; align-items: center; gap: 5px; }
  .contact-row svg { width: 8px; height: 8px; fill: var(--brand-blue); }
  .letter-body {
    position: absolute; left: 80px; right: 70px; top: 175px;
    font-size: 9.5px; line-height: 1.5;
  }
  .recipient p { margin-bottom: 10px; }
  .salutation { font-weight: 700; font-size: 12px; margin: 14px 0 12px; }
  .paragraph { margin-bottom: 12px; }
  .closing { margin-top: 24px; }
  .signature {
    display: block; width: 170px; height: 38px; margin-top: 8px;
    border-radius: 4px;
    background: linear-gradient(90deg, #e9e9e9, #f6f6f6);
  }
  .footer-band {
    position: absolute; left: 0; bottom: 28px;
    width: 480px; height: 34px;
    background: var(--brand-blue);
    color: #fff; font-size: 10px;
    display: flex; align-items: center; padding-left: 40px;
  }
  .footer-tab {
    position: absolute; right: 0; bottom: 28px;
    width: 114px; height: 34px; background: var(--grey-band);
  }
  .footer-mark {
    position: absolute; left: 462px; bottom: 25px;
    width: 40px; height: 40px; border-radius: 50%;
    background: var(--paper); border: 4px solid var(--brand-blue);
  }
</style>
</head>
<body>
  <main class="letterhead">
    <header class="masthead">
      <div class="brand">
        <span class="brand-mark"></span>
        <span class="brand-name">Harbor Stagecraft<br>Collective</span>
      </div>
      <div class="contact">
        <div class="contact-company">Harbor Stagecraft Collective, Inc</div>
        <div class="contact-row">
          <svg viewBox="0 0 10 10"><path d="M2 1h2l1 2-1 1a5 5 0 0 0 2 2l1-1 2 1v2c0 1-1 1-1 1A8 8 0 0 1 1 2c0 0 0-1 1-1z"/></svg>
          213-584-2760
        </div>
        <div class="contact-row">
          <svg viewBox="0 0 10 10"><path d="M0 2h10v6H0z M0 2l5 3 5-3" /></svg>
          admin@hsccrew.example
        </div>
        <div class="contact-row">
          <svg viewBox="0 0 10 10"><circle cx="5" cy="5" r="4.5"/></svg>
          www.hsccrew.example
        </div>
      </div>
    </header>

    <section class="letter-body">
      <div class="recipient">
        <p>Feb-03-2022</p>
        <p>Mr. Dana Whitfield<br>President</p>
        <p>Alder Corporation<br>123 Street Name, Suite# 10<br>City, State, 120023</p>
      </div>
      <p class="salutation">Dear Mr. Whitfield</p>
      <p class="paragraph">Lorem ipsum dolor sit amet, consectetur adipisicing elit, sed do eiusmod tempor incididunt ut labore et dolore magna aliqua. Ut enim ad minim veniam, quis nostrud exercitation ullamco laboris nisi ut aliquip ex ea commodo consequat. Duis aute irure dolor in reprehenderit in voluptate velit esse cillum dolore eu fugiat nulla pariatur.</p>
      <p class="paragraph">Lorem ipsum dolor sit amet, consectetur adipisicing elit, sed do eiusmod tempor incididunt ut labore et dolore magna aliqua. Ut enim ad minim veniam, quis nostrud exercitation ullamco laboris nisi ut aliquip ex ea commodo consequat. Duis aute irure dolor in reprehenderit in voluptate velit esse cillum dolore eu fugiat nulla pariatur.</p>
      <p class="paragraph">Lorem ipsum dolor sit amet, consectetur adipisicing elit, sed do eiusmod tempor incididunt ut labore et dolore magna aliqua. Ut enim ad minim veniam, quis nostrud exercitation ullamco laboris nisi ut aliquip ex ea commodo consequat.</p>
      <p class="paragraph">Excepteur sint occaecat cupidatat non proident, sunt in culpa qui officia deserunt mollit anim id est laborum. re et dolore magnam aliquam quaerat voluptatem.</p>
      <div class="closing">
        <p>Regards</p>
        <span class="signature" role="img" aria-label="Handwritten signature of Elliot Marsh"></span>
      </div>
    </section>

    <footer>
      <div class="footer-band">27410 Marlowe Blvd Ste 4, Santa Fe Springs, CA 90512</div>
      <div class="footer-tab"></div>
      <span class="footer-mark"></span>
    </footer>
  </main>
</body>
</html>
```